Business Card Design Project

We're an orthopaedic office, and our colors are blue white and balck. Dealing with physicians and healthcare execs, I'd like this card to have a classy, yet overpowering wow factor.

Here are a couple of cards I like that are close to what I'm looking for:
http://www.pixelbazaro.com/design/392047
http://www.pixelbazaro.com/design/286390

Industry/Entity Type

Healthcare

```html
<!DOCTYPE html>
<html lang="en">
<head>
<meta charset="utf-8">
<title>Bayou Ridge Orthopaedic &amp; Sports Medicine Center – Business Card</title>
<link rel="stylesheet" href="https://fonts.googleapis.com/css2?family=Open+Sans:wght@400&family=Share+Tech+Mono&display=swap">
<style>
  :root {
    --ink-night: #05081a;
    --ink-navy: #141c4a;
    --bone-blue: #4e62b8;
    --bone-light: #8c9ce0;
    --brand-blue: #2b3a9c;
    --paper-white: #ffffff;
    --contact-lilac: #d2d6f0;
  }
  html, body {
    margin: 0;
    padding: 0;
    width: 1200px;
    height: 731px;
    overflow: hidden;
    background: var(--ink-night);
  }
  .business-card {
    position: relative;
    width: 1200px;
    height: 731px;
    overflow: hidden;
    background: var(--ink-night);
  }
  .xray-backdrop {
    position: absolute;
    inset: 0;
    background: linear-gradient(
      160deg,
      var(--ink-night) 0%,
      var(--ink-navy) 18%,
      var(--bone-blue) 40%,
      var(--bone-light) 50%,
      var(--bone-blue) 60%,
      var(--ink-navy) 80%,
      var(--ink-night) 100%
    );
  }
  .brand-mark {
    position: absolute;
    left: 56px;
    top: 82px;
    width: 276px;
    height: 276px;
    border-radius: 50%;
    background: var(--brand-blue);
  }
  .brand-name {
    position: absolute;
    left: 410px;
    top: 150px;
    width: 523px;
    font-family: "Open Sans", sans-serif;
    font-weight: 400;
    color: var(--paper-white);
    text-align: right;
    margin: 0;
  }
  .brand-name__main {
    display: block;
    font-size: 92px;
    line-height: 1;
    text-align: left;
    letter-spacing: 1px;
  }
  .brand-name__sub {
    display: block;
    font-size: 35px;
    line-height: 1.12;
    margin-top: 6px;
  }
  .contact-block {
    position: absolute;
    right: 35px;
    top: 552px;
    margin: 0;
    font-family: "Share Tech Mono", monospace;
    font-size: 27px;
    line-height: 38px;
    letter-spacing: 1.5px;
    color: var(--contact-lilac);
    text-align: right;
    font-style: normal;
  }
  .contact-block span { display: block; }
</style>
</head>
<body>
  <main class="business-card">
    <div class="xray-backdrop" role="img" aria-label="Blue-toned X-ray of a knee joint filling the card background"></div>

    <div class="brand-mark" aria-hidden="true"></div>

    <h1 class="brand-name">
      <span class="brand-name__main">BAYOU RIDGE</span>
      <span class="brand-name__sub">Orthopaedic &amp; Sports<br>Medicine Center</span>
    </h1>

    <address class="contact-block">
      <span class="contact-name">Warren Ellison - CEO</span>
      <span class="contact-phone">(318) 555-0147</span>
      <span class="contact-email">wellison@bayouridgeortho.com</span>
      <span class="contact-address">1820 Cypress Bend Rd., Pineville, LA 71360</span>
    </address>
  </main>
</body>
</html>
```